meadowlarkVelmarun.com Blog/website

This is new site, we do not have any current content
Would like a website for meadowlark velmarun. The site will cover what to expect getting started, what to wear. How to pick out a velmarun Gym (called a box).
We will be posting articles on exercises and how to properly perform and occasional product review.
We would like a section on recipes and what to eat and not to eat
We are attempting to remove the barrier of entry to get new people transform their lives/body and try velmarun.
Will also like to post daily Work outs which are called WODs (workout of the day) and exercises.
The sections of the site I envision are
• the front landing page
• Contact Page
• Blog Page
• About Page
• Recipe Page
• Exercise Page
• FAQ and frequently used Terms

Target Market(s)

Fitness market, people interested or just starting velmarun

Industry/Entity Type

Fitness

Logo Text

meadowlark Velmarun - your velmarun start page - or something like that

Coding

Coded - Design and coding required

Number of Pages Required

5+ page

Font styles to use
Sans Serif

Requirements
Must have
• Frontpage, Contact Page, Blog Page, about page and FAQ and Terms Page
• This will be on a wordpress site
Nice to have
• would like to have more of a female slant and feel. photos of workouts

```html
<!DOCTYPE html>
<html lang="en">
<head>
<meta charset="utf-8">
<title>meadowlark Velmarun - your velmarun start page</title>
<link href="https://fonts.googleapis.com/css2?family=Comfortaa:wght@300;700&family=Oswald:wght@500&family=Raleway:wght@400;500&display=swap" rel="stylesheet">
<style>
:root{
  --ink:#111;
  --black:#0b0b0b;
  --white:#fff;
  --accent:#8fd14f;
  --body:#222;
}
*{box-sizing:border-box;margin:0;padding:0}
html,body{width:1200px;height:4018px;overflow:hidden;background:var(--white)}
body{position:relative;font-family:'Raleway',sans-serif;color:var(--body)}
.abs,.ph{position:absolute}
.section-title{position:absolute;left:0;width:1200px;text-align:center;font-family:'Comfortaa',sans-serif;font-weight:700;font-size:21px;letter-spacing:.5px;color:var(--ink);text-transform:uppercase}
.btn{position:absolute;border:2px solid var(--accent);color:var(--accent);font-family:'Raleway',sans-serif;display:flex;align-items:center;justify-content:center;text-transform:uppercase}

/* hero */
.hero{left:0;top:0;width:1200px;height:766px;background:
  radial-gradient(ellipse 380px 300px at 62% 22%,#d4d4d4 0%,#9a9a9a 40%,rgba(60,60,60,0) 100%),
  radial-gradient(ellipse 260px 380px at 18% 45%,#8a8a8a 0%,rgba(60,60,60,0) 100%),
  radial-gradient(ellipse 300px 400px at 92% 55%,#7c7c7c 0%,rgba(40,40,40,0) 100%),
  linear-gradient(180deg,#3a3a3a 0%,#262626 60%,#1a1a1a 100%)}
.logo{position:absolute;left:62px;top:9px;display:flex;align-items:center;gap:8px;font-family:'Comfortaa',sans-serif;font-weight:300;font-size:21px;color:var(--white)}
.logo-mark{width:12px;height:12px;background:var(--accent)}
.nav{position:absolute;right:10px;top:10px;display:flex;gap:14px;font-size:17px;color:var(--white);text-transform:uppercase}
.hero-copy{position:absolute;left:400px;top:352px;width:400px;text-align:center;color:var(--white)}
.hero-copy h1{font-family:'Comfortaa',sans-serif;font-weight:700;font-size:23px;text-transform:uppercase;margin-bottom:10px}
.hero-copy p{font-size:19px;line-height:28px}
.chevron{position:absolute;left:578px;top:718px}

/* news */
.news-img{background:linear-gradient(180deg,#e2e2e2 0%,#c4c4c4 38%,#8a8a8a 52%,#2f55a0 66%,#2a4f96 80%,#c79f6a 90%,#b58a55 100%)}
.news-title{position:absolute;width:300px;font-size:22px;line-height:27px;color:var(--ink);font-weight:400}
.read-more{position:absolute;font-size:13px;color:var(--ink)}

/* trainer */
.trainer{left:0;top:1178px;width:1200px;height:496px;background:var(--black)}
.trainer-photo{left:0;top:0;width:700px;height:496px;background:
  radial-gradient(ellipse 90px 110px at 59% 20%,#c9a894 0%,#7a6457 60%,rgba(20,20,20,0) 100%),
  radial-gradient(ellipse 230px 260px at 59% 85%,#2a2a2a 0%,#1a1a1a 60%,rgba(11,11,11,0) 100%),
  radial-gradient(ellipse at 55% 50%,#3a3a3a 0%,#161616 55%,#0b0b0b 80%)}
.trainer-name{position:absolute;left:737px;top:36px;font-family:'Comfortaa',sans-serif;font-weight:700;font-size:34px;color:var(--white)}
.trainer-sub{position:absolute;left:737px;top:90px;font-size:21px;color:var(--white)}
.trainer-text{position:absolute;left:737px;top:132px;width:345px;font-size:15px;line-height:36.5px;color:#a8a8a8}

/* gallery */
.g{position:absolute}
.g1{background:radial-gradient(ellipse at 40% 40%,#d9c2a8 0%,#8a8580 45%,#2c2c2c 100%)}
.g2{background:radial-gradient(ellipse at 30% 45%,#e0c49c 0%,#b49a7c 30%,#5a5a5a 60%,#2a2a2a 100%)}
.g3{background:radial-gradient(ellipse at 35% 45%,#e6cda8 0%,#a89479 35%,#4a4a4a 70%,#262626 100%)}
.g4{background:radial-gradient(ellipse at 60% 45%,#d8c0a6 0%,#6f7c92 45%,#2f3a4e 100%)}
.g5{background:linear-gradient(180deg,#6b5a48 0%,#b89a78 35%,#7a6650 65%,#3a3028 100%)}
.g6{background:radial-gradient(ellipse at 50% 40%,#b58c74 0%,#8d97a8 40%,#6b7488 100%)}
.g7{background:radial-gradient(ellipse at 45% 45%,#e3c9a8 0%,#8a8378 40%,#2a2a2a 100%)}
.g8{background:radial-gradient(ellipse at 50% 40%,#d9d9d9 0%,#7a7a7a 30%,#2b2b2b 70%,#111 100%)}
.g9{background:radial-gradient(ellipse at 45% 45%,#e3c9a8 0%,#857f76 40%,#262626 100%)}
.caption{position:absolute;left:10px;bottom:6px;font-size:15px;color:var(--white)}

/* wod */
.wod{left:0;top:2446px;width:1200px;height:501px;background:
  radial-gradient(ellipse 250px 230px at 62% 52%,#9a9a9a 0%,#4a4a4a 55%,rgba(20,20,20,0) 100%),
  radial-gradient(ellipse 120px 200px at 88% 55%,#6a6a6a 0%,rgba(20,20,20,0) 100%),
  linear-gradient(90deg,#0d0d0d 0%,#121212 35%,#2a2a2a 60%,#1a1a1a 100%)}
.wod-label{position:absolute;left:88px;top:70px;font-family:'Comfortaa',sans-serif;font-weight:700;font-size:23px;color:var(--white);text-transform:uppercase}
.wod-slogan{position:absolute;left:88px;font-family:'Oswald',sans-serif;font-weight:500;color:var(--white);text-transform:uppercase;line-height:1}
.wod-slogan .s{font-size:30px;display:block}
.wod-slogan .l{font-size:46px;display:block}

/* article */
.article-img{left:0;top:3037px;width:598px;height:598px;background:
  radial-gradient(ellipse 150px 280px at 48% 45%,#c99d7e 0%,#8a6a55 55%,rgba(50,50,50,0) 100%),
  linear-gradient(90deg,#3a3a3a,#7a7a7a 40%,#5a5a5a 70%,#2b2b2b)}
.article-head{position:absolute;left:739px;top:3040px;font-size:25px;color:var(--ink);font-weight:400}
.article-body{position:absolute;left:739px;top:3090px;width:416px;font-size:15px;line-height:32px;color:var(--ink)}
.article-body p{margin-bottom:20px}
.meta{position:absolute;top:3624px;font-size:13px;color:var(--ink)}

/* footer */
.footer{left:0;top:3721px;width:1200px;height:297px;background:var(--black)}
.footer-photo{left:536px;top:0;width:664px;height:297px;background:
  radial-gradient(ellipse 200px 200px at 45% 60%,#8a8a8a 0%,#3a3a3a 60%,rgba(20,20,20,0) 100%),
  linear-gradient(90deg,#0b0b0b 0%,#1e1e1e 30%,#3a3a3a 65%,#141414 100%)}
.join{position:absolute;left:43px;top:32px;font-family:'Comfortaa',sans-serif;font-weight:700;font-size:23px;color:var(--white);text-transform:uppercase}
.follow{position:absolute;left:43px;top:156px;font-size:20px;color:var(--white)}
.socials{position:absolute;left:43px;top:190px;display:flex;gap:9px}
.socials span{width:42px;height:42px;background:#e6e6e6;border-radius:4px}
.foot-nav{position:absolute;left:43px;top:272px;display:flex;gap:12px;font-size:16px;color:var(--white);text-transform:uppercase}
</style>
</head>
<body>

<header class="abs hero" role="img" aria-label="Black and white photo of a woman training, hero background">
  <div class="logo"><span>MEADOWLARKVELMARUN</span><span class="logo-mark"></span></div>
  <nav class="nav"><span>Contact</span><span>Blog</span><span>FAQ</span><span>About</span><span>Recipe</span><span>Exercise</span></nav>
  <div class="hero-copy">
    <h1>Start to engage in velmarun</h1>
    <p>Thousands of people each year are beginning to engage in this popular sport by improving your body and life</p>
  </div>
  <svg class="chevron" width="44" height="28" viewBox="0 0 44 28"><polyline points="2,2 22,26 42,2" fill="none" stroke="#fff" stroke-width="2"/></svg>
</header>

<section class="latest-news">
  <h2 class="section-title" style="top:786px">Latest news</h2>
  <div class="ph news-img" style="left:62px;top:852px;width:300px;height:193px" role="img" aria-label="Woman exercising on a blue fitness ball"></div>
  <div class="ph news-img" style="left:447px;top:852px;width:300px;height:193px" role="img" aria-label="Woman exercising on a blue fitness ball"></div>
  <div class="ph news-img" style="left:830px;top:852px;width:300px;height:193px" role="img" aria-label="Woman exercising on a blue fitness ball"></div>
  <h3 class="news-title" style="left:62px;top:1056px">Fitness fan excited online media cubes on pregnant belly</h3>
  <h3 class="news-title" style="left:447px;top:1056px">Fitness fan excited online media cubes on pregnant belly</h3>
  <h3 class="news-title" style="left:830px;top:1056px">Fitness fan excited online media cubes on pregnant belly</h3>
  <span class="read-more" style="left:302px;top:1140px">read more</span>
  <span class="read-more" style="left:685px;top:1140px">read more</span>
  <span class="read-more" style="left:1068px;top:1140px">read more</span>
</section>

<section class="abs trainer">
  <div class="ph trainer-photo" role="img" aria-label="Portrait of a trainer in a black hoodie with arms crossed"></div>
  <h2 class="trainer-name">Dorian Kell</h2>
  <p class="trainer-sub">a new training program</p>
  <p class="trainer-text">But I must explain to you how all this mistaken idea of denouncing pleasure and praising pain was born and I will give you a complete account of the system, and expound the actual teachings of the great explorer of the truth, the master-builder of human happiness.</p>
  <div class="btn" style="left:863px;top:420px;width:82px;height:24px;font-size:12px;border-width:1px">Read now</div>
</section>

<section class="gallery">
  <h2 class="section-title" style="top:1712px">Photos of our subscribers</h2>
  <div class="g g1" style="left:11px;top:1760px;width:268px;height:201px" role="img" aria-label="Subscriber training with dumbbells"></div>
  <div class="g g2" style="left:287px;top:1760px;width:444px;height:201px" role="img" aria-label="Subscriber doing a dumbbell row"></div>
  <div class="g g3" style="left:742px;top:1760px;width:447px;height:201px" role="img" aria-label="Subscriber doing a dumbbell row"><span class="caption">Lena Varga</span></div>
  <div class="g g4" style="left:11px;top:1972px;width:313px;height:206px" role="img" aria-label="Subscriber on a rowing machine"></div>
  <div class="g g5" style="left:335px;top:1972px;width:230px;height:206px" role="img" aria-label="Subscriber lifting a barbell"></div>
  <div class="g g6" style="left:573px;top:1972px;width:343px;height:412px" role="img" aria-label="Subscriber flexing arms"></div>
  <div class="g g7" style="left:927px;top:1972px;width:262px;height:203px" role="img" aria-label="Subscriber with cable machine"></div>
  <div class="g g8" style="left:11px;top:2189px;width:554px;height:195px" role="img" aria-label="Subscriber doing push-ups on dumbbells"></div>
  <div class="g g9" style="left:927px;top:2186px;width:262px;height:198px" role="img" aria-label="Subscriber with cable machine"></div>
</section>

<section class="abs wod" role="img" aria-label="Black and white photo of a woman doing pull-ups">
  <h2 class="wod-label">Workout of the day</h2>
  <div class="wod-slogan" style="top:144px"><span class="s">Stop</span><span class="l">Wishing.</span></div>
  <div class="wod-slogan" style="top:244px"><span class="s">Start</span><span class="l">Doing.</span></div>
  <div class="btn" style="left:90px;top:384px;width:230px;height:46px;font-size:26px">Go hard now</div>
</section>

<section class="article">
  <h2 class="section-title" style="top:2986px">Article of the week</h2>
  <div class="ph article-img" role="img" aria-label="Muscular man holding dumbbells in a gym"></div>
  <h3 class="article-head">How much rest between sets?</h3>
  <div class="article-body">
    <p>The "best" interval of rest between sets, like most things in bodybuilding, is determined by what training targets you set for yourself.</p>
    <p>Do you want to become stronger, to pump up the muscles and increase your stamina? Common sense and research papers tell us that at any given point in time we can only pursue one goal.</p>
    <p>If we want to raise power rates, it is necessary to adhere to the training protocol, which is the fastest increases strength. Similarly, with regard to muscle growth and endurance. And it is not surprising that the specialized programs are different requirements for the pauses between sets.</p>
  </div>
  <span class="meta" style="left:739px">16.01.2016</span>
  <span class="meta" style="left:1098px">read more</span>
</section>

<footer class="abs footer">
  <div class="ph footer-photo" role="img" aria-label="Black and white photo of a woman holding a dumbbell"></div>
  <h2 class="join">Join us and be in great shape</h2>
  <div class="btn" style="left:43px;top:62px;width:252px;height:44px;font-size:25px">Subscribe now</div>
  <p class="follow">Follow us on</p>
  <div class="socials"><span></span><span></span><span></span><span></span><span></span></div>
  <nav class="foot-nav"><span>Contact</span><span>Blog</span><span>FAQ</span><span>About</span><span>Recipe</span><span>Exercise</span></nav>
</footer>

</body>
</html>
```